Talvok Engineering Business card Design

We need to make business cards for our NDT and inspection company. The company is called Talvok Engineering. We want a professional modern feel business card. We have just completed the remaking of our website and would like to have business cards with the same feel and colours. The final design should communicate professionalism and cutting edge tech.

Target Market(s)

We sell to B2B Business clients. Our customer is an engineer or decision maker in the mechanical engineering / Oil and gas field.

Contact Information for Business Card

Please see the current business cards that we have uploaded to get the details. You can also look at our Website www.talvok-eng.example for more.

Requirements
Must have
• Less is more
Nice to have
• Less is more

```html
<!DOCTYPE html>
<html lang="en">
<head>
<meta charset="utf-8">
<title>Talvok Engineering – Business Card</title>
<link rel="stylesheet" href="https://fonts.googleapis.com/css2?family=Arimo:wght@400;700&display=swap">
<style>
  :root {
    --backdrop: #2b2b2d;
    --paper: #f7f7f7;
    --navy: #1f2d5c;
    --red: #b0121b;
    --ink: #1b1b1b;
    --rule: #222;
    --back-text: #e9eef6;
  }
  * { box-sizing: border-box; margin: 0; padding: 0; }
  html, body { width: 1200px; height: 997px; overflow: hidden; }
  body {
    background: var(--backdrop);
    font-family: "Arimo", Arial, sans-serif;
    position: relative;
  }
  .card {
    position: absolute;
    width: 525px;
    height: 300px;
    border-radius: 3px;
    overflow: hidden;
    box-shadow: 0 18px 40px rgba(0,0,0,.55);
  }

  /* ---------- Back face ---------- */
  .card--back { left: 50px; top: 348px; }
  .back__photo {
    position: absolute; inset: 0;
    background:
      radial-gradient(ellipse at 65% 35%, rgba(60,110,190,.75), transparent 60%),
      radial-gradient(ellipse at 55% 80%, rgba(200,110,40,.55), transparent 55%),
      linear-gradient(135deg, #0b1428 0%, #16284f 45%, #1a1a22 100%);
  }
  .back__list {
    position: absolute;
    list-style: none;
    color: var(--back-text);
    font-size: 13px;
    line-height: 19px;
    text-shadow: 0 1px 2px rgba(0,0,0,.6);
  }
  .back__list--inspections { left: 28px; bottom: 34px; }
  .back__list--testing { right: 32px; top: 30px; }

  /* ---------- Front face ---------- */
  .card--front { left: 625px; top: 348px; background: var(--paper); }
  .front__name-mark {
    position: absolute; left: 0; right: 0; top: 40px;
    display: flex; align-items: center; justify-content: center; gap: 10px;
    color: var(--navy); font-weight: 700; font-size: 22px;
  }
  .front__name-mark .dot {
    width: 16px; height: 16px; border-radius: 50%; background: var(--red);
  }
  .front__rule {
    position: absolute; height: 1px; background: var(--rule);
  }
  .front__rule--top { left: 300px; right: 28px; top: 100px; }
  .front__rule--name { left: 156px; right: 28px; top: 160px; }
  .front__address {
    position: absolute; right: 30px; top: 168px;
    text-align: right; color: var(--navy);
    font-size: 13px; line-height: 16px;
  }
  .front__person { position: absolute; left: 26px; top: 150px; }
  .person__name { color: var(--red); font-weight: 700; font-size: 16px; }
  .person__role { color: var(--ink); font-size: 13px; }
  .front__contacts {
    position: absolute; left: 26px; top: 208px;
    list-style: none; color: var(--navy); font-size: 14px; line-height: 22px;
  }
  .front__contacts li { display: flex; align-items: center; gap: 8px; }
  .front__contacts svg { width: 16px; height: 16px; flex: none; }
  .front__bands { position: absolute; left: 0; bottom: 0; width: 525px; height: 80px; }
  .front__web {
    position: absolute; right: 26px; bottom: 26px;
    color: #fff; font-size: 14px; letter-spacing: 2px;
  }
</style>
</head>
<body>

  <section class="card card--back" aria-label="Business card back">
    <div class="back__photo" role="img" aria-label="Photo of a welder in a protective helmet with sparks flying, in deep blue and orange tones"></div>
    <ul class="back__list back__list--inspections">
      <li>API 653 Tank Inspections</li>
      <li>API 570 Pipeline Inspections</li>
      <li>API 510 Pressure Vessel Inspections</li>
      <li>Welding Inspection</li>
      <li>Electrical Inspection</li>
      <li>OCTG Inspections</li>
      <li>Lifting Equipment Inspections</li>
    </ul>
    <ul class="back__list back__list--testing">
      <li>Non-Destructive Testing</li>
      <li>UT / PT / MT / RT / VT</li>
      <li>Advanced NDT</li>
      <li>PAUT / MFL / ILI</li>
      <li>Engineering Projects</li>
    </ul>
  </section>

  <section class="card card--front" aria-label="Business card front">
    <div class="front__name-mark"><span class="dot"></span>Talvok Engineering</div>
    <div class="front__rule front__rule--top"></div>

    <div class="front__person">
      <p class="person__name">Dorian Hallet</p>
      <p class="person__role">Director</p>
    </div>
    <div class="front__rule front__rule--name"></div>

    <address class="front__address" style="font-style:normal">
      Harbor Row, Kilind Rd<br>
      P.O. BOX 40210-80100<br>
      Mombasa Kenya
    </address>

    <ul class="front__contacts">
      <li>
        <svg viewBox="0 0 16 16" aria-hidden="true"><circle cx="8" cy="8" r="8" fill="var(--red)"/><path d="M4.5 6.5c0-1 1.5-2 3.5-2s3.5 1 3.5 2l-1.3.4-.4-1H6.2l-.4 1zM5.5 8h5l.8 3.5H4.7z" fill="#fff"/></svg>
        + 254 20 555 0142/3
      </li>
      <li>
        <svg viewBox="0 0 16 16" aria-hidden="true"><circle cx="8" cy="8" r="8" fill="var(--red)"/><rect x="4" y="5.2" width="8" height="5.6" fill="none" stroke="#fff" stroke-width="1"/><path d="M4 5.2l4 3 4-3" fill="none" stroke="#fff" stroke-width="1"/></svg>
        info@talvok-eng.example
      </li>
    </ul>

    <svg class="front__bands" viewBox="0 0 525 80" aria-hidden="true">
      <path d="M0 58 L295 38 L295 44 L0 64 Z" fill="var(--red)"/>
      <path d="M0 70 L300 49 C315 48 318 20 340 18 L525 4 L525 80 L0 80 Z" fill="var(--navy)"/>
    </svg>
    <p class="front__web">www.talvok-eng.example</p>
  </section>

</body>
</html>
```